30 Day Winter Sprint

I need 11X17 poster design. I have a generic poster that I've attached but I want a much better design and color scheme to match a holiday challenge but still use our logo. All the details (please include all of the copy/text) are in the poster attached. I also included my Drevola Bootcamp logo. I want the poster to look more like a concert poster or big event poster...not a generic homemade poster like the one I provided. I can't wait to see what people come up with!

```html
<!DOCTYPE html>
<html lang="en">
<head>
<meta charset="utf-8">
<title>30 Day Winter Sprint – Drevola Bootcamp</title>
<link href="https://fonts.googleapis.com/css2?family=Jost:wght@300;400;500;600;700&display=swap" rel="stylesheet">
<style>
  :root {
    --page: #d6d6d6;
    --ink: #ffffff;
    --accent: #e3131b;
    --night: #07060c;
    --violet: #3b1670;
    --magenta: #b02fc0;
    --band-red: #9c0d10;
  }
  * { box-sizing: border-box; margin: 0; padding: 0; }
  html, body {
    width: 1200px; height: 1000px; overflow: hidden;
    background: var(--page);
    font-family: "Jost", "Futura", sans-serif;
  }
  .poster {
    position: absolute; left: 357px; top: 135px;
    width: 487px; height: 729px; overflow: hidden;
    color: var(--ink);
    background:
      radial-gradient(ellipse 60% 30% at 25% 8%, rgba(150,70,230,.55), transparent 70%),
      radial-gradient(ellipse 55% 45% at 60% 55%, rgba(90,40,170,.45), transparent 70%),
      linear-gradient(180deg, #12081f 0%, #1a0c33 40%, #140a26 70%, var(--night) 100%);
  }
  .athlete-photo {
    position: absolute; left: 236px; top: 150px; width: 251px; height: 487px;
    background:
      radial-gradient(ellipse 40% 60% at 55% 45%, rgba(190,120,100,.55), transparent 70%),
      radial-gradient(ellipse 70% 50% at 85% 70%, rgba(200,60,220,.55), transparent 75%),
      linear-gradient(90deg, rgba(80,40,150,0), rgba(120,40,170,.5) 35%);
  }
  .brand {
    position: absolute; left: 26px; top: 64px; width: 190px;
    display: flex; align-items: center; gap: 10px;
    font-weight: 700; font-size: 22px; line-height: 1.05; letter-spacing: .5px;
    text-transform: uppercase; color: var(--ink);
  }
  .brand-mark { flex: none; width: 14px; height: 14px; background: var(--ink); }
  .title { position: absolute; left: 240px; top: 22px; line-height: 1; font-weight: 700; }
  .title-number { display: block; color: var(--accent); font-size: 48px; letter-spacing: 1px; }
  .title-line { display: block; font-size: 30px; margin-top: 2px; text-transform: uppercase; }
  .promo-band {
    position: absolute; left: 0; top: 133px; width: 380px; height: 39px;
    background: linear-gradient(90deg, var(--band-red) 0%, #7a0a0e 70%, rgba(122,10,14,0) 100%);
    padding: 5px 0 0 25px;
    font-size: 11px; font-weight: 600; line-height: 1.3; text-transform: uppercase;
  }
  .intro {
    position: absolute; left: 25px; top: 192px; width: 280px;
    font-size: 15px; font-weight: 400; line-height: 1.2; text-transform: uppercase;
  }
  .offer-heading { position: absolute; left: 25px; top: 281px; font-size: 12px; font-weight: 600; }
  .benefits {
    position: absolute; left: 25px; top: 304px; width: 262px; list-style: none;
    font-size: 9px; font-weight: 500; line-height: 1.25;
  }
  .benefits li { position: relative; padding-left: 8px; margin-bottom: 10px; }
  .benefits li::before {
    content: ""; position: absolute; left: 0; top: 4px;
    width: 3px; height: 3px; border-radius: 50%; background: var(--accent);
  }
  .pricing {
    position: absolute; left: 25px; top: 434px;
    font-size: 15px; font-weight: 600; line-height: 1.2; text-transform: uppercase;
  }
  .pricing .price { color: var(--accent); }
  .pricing .client-rate { font-size: 13px; display: block; margin-top: 8px; }
  .phone-line { position: absolute; left: 25px; top: 552px; display: flex; align-items: center; gap: 8px; }
  .phone-number { font-size: 33px; font-weight: 600; letter-spacing: .3px; }
  .closing-band {
    position: absolute; left: 0; bottom: 0; width: 100%; height: 92px;
    background: var(--night); text-align: center; padding-top: 12px;
  }
  .deadline { font-size: 19px; font-weight: 600; }
  .deadline .urgent { color: var(--accent); }
  .claim { font-size: 13px; font-weight: 400; margin-top: 4px; text-transform: uppercase; }
  .site { font-size: 12px; margin-top: 2px; }
</style>
</head>
<body>
  <main class="poster">
    <div class="athlete-photo" role="img" aria-label="Photo of a fit woman in black sportswear and a wrist wrap, lit by purple electric light"></div>

    <div class="brand"><span class="brand-mark"></span><span>Drevola<br>Bootcamp</span></div>

    <h1 class="title">
      <span class="title-number">30- DAY</span>
      <span class="title-line">Winter</span>
      <span class="title-line">Sprint</span>
    </h1>

    <p class="promo-band">Discover the secret to losing weight this holiday<br>season in just 30 days with this amazing new program!</p>

    <p class="intro">Imagine... a training and nutrition program so efective, you could get 3x the fat loss in just 30 days-during the holidays!!!</p>

    <h2 class="offer-heading">Here's what you get starting november 3rd, 2014:</h2>
    <ul class="benefits">
      <li>Training sessions designed to incinerate fat off your midsection, thighs and arms.</li>
      <li>Fat-melting nutrition guides, stress management tips, delicious recipes, and BONUS workouts.</li>
      <li>A Success Sesion to map out your individual plan for success</li>
      <li>Access to our Drevola VIP Accountability page to ensure you get results.</li>
    </ul>

    <p class="pricing">
      You get all this a <span class="price">$299</span> value<br>
      for only <span class="price">$69!</span>
      <span class="client-rate">(Clients <span class="price">$39</span>)</span>
    </p>

    <div class="phone-line">
      <svg width="31" height="54" viewBox="0 0 31 54" aria-hidden="true">
        <rect x="2" y="2" width="27" height="50" rx="4" fill="none" stroke="#fff" stroke-width="3"/>
        <line x1="2" y1="42" x2="29" y2="42" stroke="#fff" stroke-width="2.5"/>
        <circle cx="15.5" cy="47" r="2" fill="#fff"/>
      </svg>
      <span class="phone-number">555-014-2870</span>
    </div>

    <footer class="closing-band">
      <p class="deadline">HURRY! <span class="urgent">Registration closes thursday Oct. 30th!!!</span></p>
      <p class="claim">Claim your spot now&nbsp; 555-014-2870</p>
      <p class="site">www.drevola-fit.com</p>
    </footer>
  </main>
</body>
</html>
```